Banner Ad in Spanish for Car Accident Law Firm in Miami Florida

I need a Banner Ad in Spanish Language. We are an Accident Law Firm in Miami, FL. We help injured people. I need a Banner Ad with a Vibrant Colorful Background to Stand Out. A Click-Able Call to Action is needed. We don't want to make the banner too crowded and we want the message to be simple to understand. We are looking for a skilled graphic designer to create a visually appealing banner ad for our YouTube marketing campaign. The required dimensions and format are:
1920 x 275
.png & .mp4

The Banner is for our Plaintiff’s Personal Injury Law Firm. We represent Spanish Speaking clients who are injured in CAR ACCIDENTS. As such the banner must include:
1. Our Firm Logo
2. Our Telephone# (305) 471-6023
3. Stock Photo of Car Crash
4. Photo of our attorney in office
5. The Words Abogados de Accidentes
The telephone number should be fairly large and stand out it is our call to action. The words Abogados de Accidentes should be close to our Logo to associate the two.

Target Market(s)

Car Accident Victims who speak Spanish

Industry/Entity Type

Legal, Law Firm.

Font styles to use
Sans Serif

Colors
59FF00
82FF00
B8FF75
E3FFCB
F4FFEA
F0912C
F2A743
F7CA91
FBE8D2
FDF5EE
6B429C
8869AF
B7A5CE
E3DAEB
F3F0F8

Requirements
Must have
• A bold background so that Banner Ad can be seen on mobile and against the screen being advertising against
Should not have
• Be too crowded. Hard to understand what it is for.

```html
<!DOCTYPE html>
<html lang="es">
<head>
<meta charset="utf-8">
<title>Marlowe Law Firm – Abogados de Accidentes</title>
<link rel="stylesheet" href="https://fonts.googleapis.com/css2?family=Archivo+Black&family=Poppins:wght@400;600;700;800&display=swap">
<style>
  :root {
    --purple-deep: #4b2a7a;
    --purple: #6b429c;
    --purple-mid: #8869af;
    --lavender: #e3daeb;
    --lavender-pale: #f3f0f8;
    --green: #82ff00;
    --green-soft: #b8ff75;
    --orange: #f0912c;
    --orange-pale: #fbe8d2;
    --photo-grey-1: #c9c9cb;
    --photo-grey-2: #6e6e72;
    --car-1: #1b2130;
    --car-2: #3b4456;
  }
  * { margin: 0; padding: 0; box-sizing: border-box; }
  html, body { width: 1200px; height: 172px; overflow: hidden; background: var(--lavender-pale); }
  .banner {
    position: relative;
    width: 1200px;
    height: 172px;
    overflow: hidden;
    background: linear-gradient(90deg, var(--lavender) 0%, var(--lavender-pale) 30%, #ffffff 50%, var(--lavender-pale) 70%, var(--orange-pale) 100%);
    font-family: "Poppins", sans-serif;
    color: var(--purple-deep);
  }
  .accent-bar {
    position: absolute;
    left: 0;
    bottom: 0;
    width: 100%;
    height: 5px;
    background: linear-gradient(90deg, var(--green) 0%, var(--green-soft) 40%, var(--orange) 100%);
  }
  .brand {
    position: absolute;
    left: 26px;
    top: 17px;
    display: flex;
    align-items: center;
    gap: 8px;
  }
  .brand-square {
    width: 44px;
    height: 44px;
    border-radius: 6px;
    background: var(--purple);
  }
  .brand-name {
    font-weight: 600;
    color: var(--purple-deep);
    line-height: 1;
  }
  .brand-name .firm { display: block; font-size: 22px; letter-spacing: 0.5px; }
  .brand-name .suffix {
    display: flex;
    align-items: center;
    justify-content: flex-end;
    gap: 4px;
    font-size: 9px;
    letter-spacing: 1.5px;
    margin-top: 3px;
  }
  .brand-name .suffix::before {
    content: "";
    display: block;
    width: 52px;
    height: 1px;
    background: var(--purple-deep);
  }
  .attorney-photo {
    position: absolute;
    left: 226px;
    top: 8px;
    width: 120px;
    height: 164px;
    border-radius: 50px 50px 0 0;
    background: linear-gradient(180deg, var(--photo-grey-1) 0%, var(--photo-grey-2) 100%);
  }
  .attorney-credit {
    position: absolute;
    right: 992px;
    top: 117px;
    text-align: right;
    line-height: 1.05;
    color: var(--purple-deep);
  }
  .attorney-credit .name { font-weight: 800; font-size: 15px; display: block; }
  .attorney-credit .quals { font-weight: 400; font-size: 15px; display: block; }
  .headline {
    position: absolute;
    left: 428px;
    top: 30px;
    width: 372px;
    font-family: "Archivo Black", sans-serif;
    font-weight: 400;
    color: var(--purple);
    text-align: center;
    line-height: 0.95;
  }
  .headline .line1, .headline .line2 { display: block; font-size: 44px; letter-spacing: 0.5px; }
  .headline .line2 { margin-top: 2px; }
  .cta {
    position: absolute;
    left: 516px;
    top: 133px;
    display: flex;
    align-items: center;
    gap: 7px;
    text-decoration: none;
    color: var(--purple-deep);
  }
  .cta svg { width: 21px; height: 29px; display: block; }
  .cta .number { font-weight: 700; font-size: 24px; letter-spacing: 0.3px; line-height: 1; }
  .crash-photo {
    position: absolute;
    left: 934px;
    top: 0;
    width: 266px;
    height: 172px;
    border-radius: 60px 0 0 0;
    background: linear-gradient(135deg, var(--car-2) 0%, var(--car-1) 70%);
  }
</style>
</head>
<body>
  <div class="banner">
    <div class="brand">
      <div class="brand-square"></div>
      <div class="brand-name">
        <span class="firm">MARLOWE</span>
        <span class="suffix">LAW FIRM</span>
      </div>
    </div>

    <div class="attorney-photo" role="img" aria-label="Foto del abogado en traje, en la oficina"></div>

    <div class="attorney-credit">
      <span class="name">NAME</span>
      <span class="quals">QUALIFICATIONS</span>
    </div>

    <h1 class="headline">
      <span class="line1">ABOGADOS DE</span>
      <span class="line2">ACCIDENTES</span>
    </h1>

    <a class="cta" href="tel:+13054716023">
      <svg viewBox="0 0 21 28" aria-hidden="true">
        <rect x="0" y="0" width="21" height="28" rx="3" fill="var(--orange)"/>
        <path d="M6.5 7.5c.6-.6 1.4-.6 1.9 0l1.2 1.6c.4.5.3 1.2-.1 1.6l-.8.7c.5 1.6 1.6 3 3 3.9l.8-.6c.5-.4 1.2-.3 1.6.2l1.1 1.6c.4.6.3 1.3-.2 1.8l-.7.6c-.8.7-2 .8-3 .3-3.1-1.6-5.2-4.6-5.6-8-.1-1 .3-2 1-2.7z" fill="#ffffff"/>
      </svg>
      <span class="number">(305) 471-6023</span>
    </a>

    <div class="crash-photo" role="img" aria-label="Foto de un coche oscuro con la parte delantera destrozada tras un accidente"></div>

    <div class="accent-bar"></div>
  </div>
</body>
</html>
```